Need Bus charter business website,

I am starting a bus charter business in the near future. I am based in Geelong, Victoria in Australia. I will have a 25 or 28 seater bus that will be used to take people on charted trips. Whether they be to birthday parties, weddings, sporting events, corporate events, mystery trips, going down the Great Ocean Road, or anywhere someone wants. As for colour scheme, I'm leaning towards something blue and grey, but open to anything really that catches my eye. I played around with a basic web design program and made a basic site which I uploaded ( www.kelvomtravel.com.au) It has things which I wanted to include such as, services I will provide, trip information, contact form etc.

I don't mind if the layout is completely different to my site as it was only a template that was included in the program I used. I would like the overall design to be relatively fluid, not having to back-track a lot to navigate the site.

```html
<!DOCTYPE html>
<html lang="en">
<head>
<meta charset="utf-8">
<title>Kelvom Travel – Bus Charter Geelong</title>
<link href="https://fonts.googleapis.com/css2?family=Roboto:wght@300;400;500;700&display=swap" rel="stylesheet">
<style>
:root{
  --blue:#0a74d6;
  --blue-dark:#0660b4;
  --ink:#222;
  --text:#555;
  --muted:#999;
  --rule:#e3e3e3;
  --topbar:#1d1d1d;
  --footer:#0d0d0f;
  --field:#e9e9e9;
  --panel:#f6f6f6;
  --white:#fff;
}
*{box-sizing:border-box;margin:0;padding:0}
html,body{width:840px;height:1200px;overflow:hidden;background:var(--white)}
body{font-family:"Roboto",Arial,sans-serif;color:var(--ink);position:relative}
.abs{position:absolute}

/* top bar */
.topbar{left:0;top:0;width:840px;height:30px;background:var(--topbar)}
.topbar .call{left:120px;top:8px;font-size:9.5px;color:var(--white);font-weight:500;display:flex;align-items:center;gap:6px}
.topbar .call svg{width:15px;height:12px}
.topbar .call .num{color:var(--blue);margin-left:4px;font-weight:400}
.social-top{left:622px;top:5px;display:flex;gap:6px}
.social-top span{width:19px;height:19px;border:1px solid #3a3a3a;display:block;position:relative}
.social-top span::after{content:"";position:absolute;left:6px;top:6px;width:5px;height:5px;background:var(--blue)}

/* header */
.header{left:0;top:30px;width:840px;height:87px;background:var(--white)}
.brand{left:121px;top:27px;font-size:18px;font-weight:500;color:var(--ink);letter-spacing:.3px;display:flex;align-items:center;gap:8px}
.brand i{width:10px;height:10px;background:var(--blue);display:block}
.nav{left:391px;top:0;height:87px;display:flex;font-size:9px;font-weight:400}
.nav a{color:var(--ink);text-decoration:none;height:87px;line-height:87px;padding:0 9px}
.nav a.active{background:var(--blue);color:var(--white);width:57px;text-align:center;padding:0;margin-right:10px}

/* hero */
.hero{left:0;top:117px;width:840px;height:263px;background:linear-gradient(100deg,#6b5a44 0%,#9aa2a8 30%,#c9d3dc 55%,#b9c9d8 75%,#7a7060 100%)}
.hero-banner{left:0;top:69px;width:516px;height:124px}
.hero-title{left:122px;top:98px;color:var(--white)}
.hero-title .l1{font-size:25px;font-weight:300;letter-spacing:.3px}
.hero-title .l2{font-size:38px;font-weight:700;letter-spacing:1px;margin-top:-4px}
.dots{left:125px;top:170px;display:flex;gap:3px}
.dots span{width:6px;height:6px;border-radius:50%;background:#7fb2e4}
.dots span:first-child{background:var(--white)}

/* intro */
.intro-title{left:121px;top:397px;font-size:21px;font-weight:300;line-height:25px;color:#333}
.intro-title em{font-style:normal;color:var(--blue);font-weight:400}
.feature{display:flex;align-items:center;gap:10px;font-size:9.5px;color:#222}
.feature .ring{width:62px;height:62px;border:2px solid var(--blue);border-radius:50%;display:flex;align-items:center;justify-content:center}
.feature svg{width:26px;height:26px}
.intro-text{left:121px;top:610px;width:310px;font-size:9px;line-height:11.6px;color:var(--text)}
.btn-more{width:82px;height:36px}
.btn-more span{position:absolute;left:12px;top:13px;font-size:8px;font-weight:500;color:var(--white);letter-spacing:.3px}

/* booking panel */
.booking{left:454px;top:400px;width:266px;height:302px;background:var(--panel)}
.booking-head{left:0;top:0;width:207px;height:46px}
.booking-head span{position:absolute;left:20px;top:8px;font-size:23px;color:var(--white);font-weight:400}
.field{width:112px}
.field label{display:block;font-size:9px;color:#333;margin-bottom:6px}
.field .box{height:24px;background:var(--field);font-size:7px;color:var(--muted);padding:0 8px;line-height:24px;position:relative}
.field .box svg{position:absolute;right:7px;top:8px;width:8px;height:8px}
.btn-book{left:163px;top:256px;width:103px;height:46px}
.btn-book span{position:absolute;left:25px;top:16px;font-size:11.5px;color:var(--white)}

/* offers */
.offer-rule{height:1px;background:var(--rule);width:295px;left:120px}
.offer-title{font-size:24px;color:var(--blue);font-weight:400;letter-spacing:.2px}
.offer-sub{font-size:9px;color:#222}
.offer-photo{width:260px;height:95px}
.offer-tab{width:25px;height:95px;background:var(--blue)}
.offer-tab svg{position:absolute;left:6px;top:38px;width:13px;height:20px}

/* footer */
.footer{left:0;top:984px;width:840px;height:179px;background:radial-gradient(ellipse at 40% 60%,#1d1f24 0%,var(--footer) 70%)}
.footer h4{font-size:15px;font-weight:300;color:var(--blue);letter-spacing:.3px}
.menu{left:123px;top:20px;width:103px}
.menu ul{list-style:none;margin-top:14px}
.menu li{font-size:7.5px;color:#bbb;height:21.5px;line-height:21.5px;border-bottom:1px solid #2c2c2c;padding-left:9px;position:relative}
.menu li::before{content:"";position:absolute;left:1px;top:10px;width:2px;height:2px;background:#bbb}
.social{left:281px;top:20px;width:107px}
.social ul{list-style:none;margin-top:14px}
.social li{font-size:7.5px;color:#bbb;height:21.5px;line-height:21.5px;border-bottom:1px solid #2c2c2c;text-align:right;position:relative}
.social li::before{content:"";position:absolute;left:0;top:7px;width:7px;height:7px;border:1px solid #555}
.vrule{width:1px;height:120px;background:#2a2a2a;top:38px}
.news{left:443px;top:20px;width:110px}
.news .item{margin-top:12px}
.news .item b{display:block;font-size:7.5px;color:var(--white);font-weight:400;padding-bottom:5px;border-bottom:1px solid #333;position:relative;padding-left:7px}
.news .item b::before{content:"";position:absolute;left:0;top:3px;width:2px;height:2px;background:var(--white)}
.news .item p{font-size:7px;color:#888;line-height:9px;margin-top:4px;padding-left:4px}
.blog{left:605px;top:20px;width:130px}
.blog .post{display:flex;align-items:center;gap:5px;margin-top:12px;font-size:7.5px;color:var(--white)}
.blog .post:first-of-type{margin-top:14px}
.blog .thumb{width:43px;height:37px;background:linear-gradient(135deg,#7e8a6e,#c9c2b0 60%,#5c6a80)}
.blog .post + .post .thumb{background:linear-gradient(135deg,#8fa0b3,#e6e8ea 55%,#5b6f52)}
.bottom{left:0;top:1163px;width:840px;height:37px;text-align:center;line-height:37px;font-size:8.5px;color:#222}
</style>
</head>
<body>

<div class="abs topbar">
  <div class="abs call">
    <svg viewBox="0 0 15 12"><path d="M2 4c0-2 3-3 5.5-3S13 2 13 4l-2.5 1-.5-1.5H5L4.5 5zM3 6h9l1 5H2z" fill="#0a74d6"/></svg>
    Call Us Now ! <span class="num">( 0800-555-0192 )</span>
  </div>
  <div class="abs social-top" aria-label="Social links"><span></span><span></span><span></span><span></span></div>
</div>

<header class="abs header">
  <div class="abs brand">Kelvom Travel</div>
  <nav class="abs nav">
    <a class="active" href="#">HOME</a>
    <a href="#">ABOUT</a>
    <a href="#">BOOKING</a>
    <a href="#">OFFERS</a>
    <a href="#">SERVICES</a>
    <a href="#">CONTACT</a>
  </nav>
</header>

<section class="abs hero" role="img" aria-label="Photo of a white touring coach driving along a country road">
  <svg class="abs hero-banner" viewBox="0 0 516 124"><polygon points="0,0 450,0 516,62 450,124 0,124" fill="#0a74d6" fill-opacity=".93"/></svg>
  <div class="abs hero-title">
    <div class="l1">MAKING TRANSPORTATION</div>
    <div class="l2">FAST AND SAFE !</div>
  </div>
  <div class="abs dots"><span></span><span></span><span></span></div>
</section>

<section class="intro">
  <h2 class="abs intro-title">Explore Your Favorite Destination<br>With <em>Style And Comfort!</em></h2>

  <div class="abs feature" style="left:121px;top:459px">
    <div class="ring"><svg viewBox="0 0 26 26"><path d="M4 18a9 9 0 1 1 18 0" fill="none" stroke="#0a74d6" stroke-width="2.5"/><path d="M13 18l4-6" stroke="#0a74d6" stroke-width="2"/><rect x="8" y="19" width="10" height="3" fill="#0a74d6"/></svg></div>
    <span>FAST</span>
  </div>
  <div class="abs feature" style="left:279px;top:459px">
    <div class="ring"><svg viewBox="0 0 26 26"><path d="M8 4h6l-1 11h7l1 6H9z" fill="none" stroke="#0a74d6" stroke-width="2" stroke-linejoin="round"/><path d="M7 22h15" stroke="#0a74d6" stroke-width="2"/></svg></div>
    <span>COMFORT</span>
  </div>
  <div class="abs feature" style="left:121px;top:536px">
    <div class="ring"><svg viewBox="0 0 26 26"><path d="M13 3l8 3v6c0 6-4 9-8 11-4-2-8-5-8-11V6z" fill="#0a74d6"/><path d="M13 6v14c3-2 5-4 5-8V8z" fill="#fff" fill-opacity=".45"/></svg></div>
    <span>SAFE</span>
  </div>
  <div class="abs feature" style="left:279px;top:536px">
    <div class="ring"><svg viewBox="0 0 26 26"><path d="M1 11l5-4 4 2 3-2 4 2 4-3 4 5-4 3-6 5-3-2-3 1-4-3z" fill="#0a74d6"/><path d="M10 13l3 3M12 12l3 3" stroke="#fff" stroke-width="1"/></svg></div>
    <span>SERVICE</span>
  </div>

  <p class="abs intro-text">We are an accredited bus company that operates bus trip and charter work in the Geelong area. We offer a range of services, from day trips down the Great Ocean Road, to transport for wedding guests, Buck’s and Hen’s nights or school trips.</p>

  <a class="abs btn-more" style="left:120px;top:666px" href="#">
    <svg width="82" height="36"><polygon points="0,0 64,0 82,18 64,36 0,36" fill="#0a74d6"/></svg>
    <span>READ MORE</span>
  </a>
  <div class="abs offer-rule" style="top:702px"></div>
</section>

<aside class="abs booking">
  <div class="abs booking-head">
    <svg width="207" height="46"><polygon points="0,0 185,0 207,23 185,46 0,46" fill="#0a74d6"/></svg>
    <span>BOOK MY BUS</span>
  </div>

  <div class="abs field" style="left:21px;top:62px"><label>FROM</label><div class="box">SELECT<svg viewBox="0 0 8 8"><path d="M1 2l3 3 3-3" fill="none" stroke="#aaa"/></svg></div></div>
  <div class="abs field" style="left:134px;top:62px"><label>TO</label><div class="box">SELECT<svg viewBox="0 0 8 8"><path d="M1 2l3 3 3-3" fill="none" stroke="#aaa"/></svg></div></div>
  <div class="abs field" style="left:21px;top:110px"><label>DEPART ON</label><div class="box">05-05-2015<svg viewBox="0 0 8 8"><path d="M1 3l3-3 3 3M1 5l3 3 3-3" fill="none" stroke="#aaa"/></svg></div></div>
  <div class="abs field" style="left:134px;top:110px"><label>PASSENGERS</label><div class="box">05<svg viewBox="0 0 8 8"><path d="M1 3l3-3 3 3M1 5l3 3 3-3" fill="none" stroke="#aaa"/></svg></div></div>
  <div class="abs field" style="left:21px;top:158px"><label>SITTING OPTION</label><div class="box">ANY<svg viewBox="0 0 8 8"><path d="M1 2l3 3 3-3" fill="none" stroke="#aaa"/></svg></div></div>
  <div class="abs field" style="left:134px;top:158px"><label>MORE OPTION</label><div class="box">SELECT<svg viewBox="0 0 8 8"><path d="M1 2l3 3 3-3" fill="none" stroke="#aaa"/></svg></div></div>
  <div class="abs field" style="left:21px;top:206px"><label>DEPARTURE TIME</label><div class="box">ANY TIME<svg viewBox="0 0 8 8"><path d="M1 2l3 3 3-3" fill="none" stroke="#aaa"/></svg></div></div>
  <div class="abs field" style="left:134px;top:206px"><label>BUS TYPE</label><div class="box">ANY BUS<svg viewBox="0 0 8 8"><path d="M1 2l3 3 3-3" fill="none" stroke="#aaa"/></svg></div></div>

  <a class="abs btn-book" href="#">
    <svg width="103" height="46"><polygon points="0,23 22,0 103,0 103,46 22,46" fill="#0a74d6"/></svg>
    <span>BOOK NOW !</span>
  </a>
</aside>

<section class="offers">
  <div class="abs offer-rule" style="top:732px"></div>
  <h3 class="abs offer-title" style="left:121px;top:740px">BOOK A BUS FOR !</h3>
  <p class="abs offer-sub" style="left:121px;top:771px">FUNCTION , BIRTHDAY PARTIES , SPORTING EVENTS , MYSTRY TRIP</p>
  <a class="abs btn-more" style="left:120px;top:791px" href="#">
    <svg width="82" height="36"><polygon points="0,0 64,0 82,18 64,36 0,36" fill="#0a74d6"/></svg>
    <span>READ MORE</span>
  </a>
  <div class="abs offer-rule" style="top:828px"></div>
  <div class="abs offer-photo" style="left:434px;top:733px;background:linear-gradient(90deg,#5d7a3e 0%,#c9c4b6 35%,#e9ecee 60%,#7b8288 100%)" role="img" aria-label="Photo of a group of guests gathered beside parked coaches"></div>
  <div class="abs offer-tab" style="left:694px;top:733px"><svg viewBox="0 0 13 20"><path d="M2 1l9 9-9 9" fill="none" stroke="#fff" stroke-width="2"/></svg></div>

  <div class="abs offer-rule" style="top:850px"></div>
  <h3 class="abs offer-title" style="left:121px;top:857px">WANT TO BOOK A TRIP?</h3>
  <p class="abs offer-sub" style="left:121px;top:888px">FUNCTION , BIRTHDAY PARTIES , SPORTING EVENTS , MYSTRY TRIP</p>
  <a class="abs btn-more" style="left:120px;top:909px" href="#">
    <svg width="82" height="36"><polygon points="0,0 64,0 82,18 64,36 0,36" fill="#0a74d6"/></svg>
    <span>READ MORE</span>
  </a>
  <div class="abs offer-rule" style="top:945px"></div>
  <div class="abs offer-photo" style="left:434px;top:850px;background:linear-gradient(180deg,#b8d0e8 0%,#e4ebf2 35%,#f2f3f4 65%,#9a9a8e 100%)" role="img" aria-label="Photo of a white double-decker coach parked outdoors"></div>
  <div class="abs offer-tab" style="left:694px;top:850px"><svg viewBox="0 0 13 20"><path d="M2 1l9 9-9 9" fill="none" stroke="#fff" stroke-width="2"/></svg></div>
</section>

<footer class="abs footer" role="contentinfo">
  <div class="abs menu">
    <h4>MENU</h4>
    <ul><li>HOME</li><li>ABOUT</li><li>SERVICE</li><li>BOOKING</li><li>CONTACT</li></ul>
  </div>
  <div class="abs vrule" style="left:256px"></div>
  <div class="abs social">
    <h4>SOCIAL</h4>
    <ul><li>SOCIALIA</li><li>CHIRPER</li><li>CIRCLES</li><li>PINBOARD</li></ul>
  </div>
  <div class="abs vrule" style="left:418px"></div>
  <div class="abs news">
    <h4>NEWS</h4>
    <div class="item"><b>KELVOM TRAVEL :</b><p>We are an accredited bus comp any that operates .</p></div>
    <div class="item"><b>KELVOM TRAVEL :</b><p>We are an accredited bus comp any that operates .</p></div>
  </div>
  <div class="abs vrule" style="left:580px"></div>
  <div class="abs blog">
    <h4>BLOG</h4>
    <div class="post"><div class="thumb" role="img" aria-label="Thumbnail photo of passengers beside a coach"></div>KELVOM TRAVEL :</div>
    <div class="post"><div class="thumb" role="img" aria-label="Thumbnail photo of a coach"></div>KELVOM TRAVEL :</div>
  </div>
</footer>

<div class="abs bottom">KELVOM TRAVEL © 2014.&nbsp; Privacy Policy</div>

</body>
</html>
```